Online trading school - Website design

We are building an online trading school (trading of shares, commodities, indices, currencies). The purpose is to teach online traders how to trade successfully. We need to design the homepage of the website and logo (bramwelloq.com will be the domain). The homepage will contain the following elements

- logo
- Sign in and Register links/buttons
- upper menu
- short introduction
- a couple of bullet points 'Why to join our school?'
- sign up form
- text
- bottom menu

Attached is a draft for the designer. The draft is just for an inspiration, the actual structure of the website can be different if the designer thinks so.

The designer is free to choose colors.

School

3 page

```html
<!DOCTYPE html>
<html lang="en">
<head>
<meta charset="utf-8">
<title>Bramwelloq – Online Trading School</title>
<link href="https://fonts.googleapis.com/css2?family=Montserrat:wght@400;500;600;700&family=Arimo:wght@400;700&display=swap" rel="stylesheet">
<style>
:root{
  --topbar:#22282e;
  --navy:#0b3f86;
  --navy-deep:#083370;
  --panel:#0f5c8e;
  --light:#ececec;
  --ink-blue:#12497b;
  --body-grey:#555;
  --white:#fff;
  --dark-btn:#1d2227;
  --footer:#1f2a33;
  --footer-line:#2d3944;
}
*{margin:0;padding:0;box-sizing:border-box}
html,body{width:1200px;height:1064px;overflow:hidden}
body{position:relative;font-family:'Arimo',Arial,sans-serif;background:var(--light);color:var(--white)}
.abs{position:absolute}

.topbar{left:0;top:0;width:1200px;height:29px;background:var(--topbar);font-size:8.5px;color:#e4e6e8}
.topbar .item{position:absolute;top:9px;display:flex;align-items:center;gap:5px}
.topbar .social{position:absolute;top:7px;left:847px;display:flex;align-items:center;gap:6px}
.topbar .dot{width:10px;height:10px;border-radius:50%;background:#c4c9ce}

.header{left:0;top:29px;width:1200px;height:131px;background:linear-gradient(180deg,var(--navy-deep),var(--navy) 60%,#1752a0)}
.photo-band{left:0;top:160px;width:1200px;height:215px;background:linear-gradient(90deg,#d9dde2,#eef0f2 50%,#d8dce1)}

.logo{left:236px;top:50px;display:flex;align-items:center;gap:8px;font-family:'Montserrat',sans-serif;font-weight:700;font-size:21px;letter-spacing:.3px}
.logo .mark{width:28px;height:28px;border-radius:50%;background:var(--white)}

.auth{top:41px;height:20px;border:1px solid #dfe6ef;font-size:8.5px;display:flex;align-items:center;justify-content:center}
.signin{left:854px;width:57px}
.register{left:917px;width:56px}

.menu{left:591px;top:73px;display:flex;gap:16px;font-family:'Montserrat',sans-serif;font-weight:600;font-size:9.5px}

.hero-frame{left:225px;top:101px;width:750px;height:274px;background:var(--white)}
.hero-image{left:231px;top:108px;width:509px;height:261px;background:radial-gradient(ellipse at 70% 40%,#1ea3c4,#0b5f86 55%,#083a5c)}
.join{left:742px;top:108px;width:225px;height:261px;background:var(--panel)}
.join h2{position:absolute;left:17px;top:22px;font-family:'Montserrat',sans-serif;font-weight:700;font-size:18px;letter-spacing:.2px}
.field{position:absolute;left:17px;width:192px;height:32px;background:var(--white);color:#333;font-size:10px;padding:11px 9px}
.agree{position:absolute;left:17px;top:174px;display:flex;align-items:center;gap:8px;font-family:'Montserrat',sans-serif;font-size:9px}
.agree .box{width:13px;height:13px;background:var(--white)}
.submit{position:absolute;left:15px;top:201px;width:85px;height:31px;background:var(--dark-btn);font-family:'Montserrat',sans-serif;font-weight:600;font-size:11px;display:flex;align-items:center;justify-content:center}

.features{left:0;top:375px;width:1200px;height:191px;background:var(--light)}
.feature{position:absolute;top:37px;width:150px;margin-left:-75px;text-align:center}
.feature .icon{width:30px;height:30px;border-radius:50%;background:var(--ink-blue);margin:0 auto;display:flex;align-items:center;justify-content:center}
.feature h3{margin-top:14px;font-family:'Montserrat',sans-serif;font-weight:600;font-size:11px;line-height:13px;color:var(--ink-blue)}
.feature p{margin-top:11px;font-size:9.5px;line-height:10.5px;color:var(--body-grey)}

.offer{left:0;top:566px;width:1200px;height:223px;background:linear-gradient(180deg,#0d4788,#104f93 60%,#0b447f);text-align:center}
.offer h2{position:absolute;left:0;width:1200px;top:47px;font-family:'Montserrat',sans-serif;font-weight:400;font-size:22px}
.offer p{position:absolute;left:280px;width:640px;top:91px;font-family:'Montserrat',sans-serif;font-size:11.6px;line-height:14.4px;color:#dfe8f3}

.footer{left:0;top:789px;width:1200px;height:237px;background:var(--footer)}
.col{position:absolute;top:37px}
.col h4{font-family:'Montserrat',sans-serif;font-weight:500;font-size:13.5px;letter-spacing:.2px}
.col ul{list-style:none;margin-top:17px}
.col li{font-size:10px;color:#dde2e6;height:18px;display:flex;align-items:center;gap:8px}
.col li .bullet{width:7px;height:7px;border-radius:50%;background:#cfd5da}
.col.connect ul{margin-top:16px}
.col.connect li{height:28.5px;gap:9px}
.col.connect .ring{width:23px;height:23px;border-radius:50%;background:#7a8289;border:2px solid #3a454f}

.bottombar{left:0;top:1026px;width:1200px;height:38px;background:var(--footer);border-top:1px solid var(--footer-line);font-size:8px;color:#d3d8dc}
.copyright{left:230px;top:13px}
.subscribe{left:477px;top:11px;font-family:'Montserrat',sans-serif;font-weight:600;font-size:10.5px;color:var(--white)}
.sub-input{left:553px;top:8px;width:163px;height:19px;background:var(--white);color:#444;font-size:9px;padding:4px 6px}
.sub-go{left:716px;top:8px;width:42px;height:19px;background:#1366a8;color:var(--white);font-family:'Montserrat',sans-serif;font-weight:600;font-size:10px;display:flex;align-items:center;justify-content:center}
.legal{left:862px;top:13px}
</style>
</head>
<body>

<div class="abs topbar">
  <div class="item" style="left:225px">
    <svg width="8" height="10" viewBox="0 0 8 10"><path d="M4 0a3.5 3.5 0 0 0-3.5 3.5C.5 6 4 10 4 10s3.5-4 3.5-6.5A3.5 3.5 0 0 0 4 0zm0 5a1.4 1.4 0 1 1 0-2.8A1.4 1.4 0 0 1 4 5z" fill="#e4e6e8"/></svg>
    <span>Lindenweg 14 40210 Halden</span>
  </div>
  <div class="item" style="left:361px">
    <svg width="6" height="10" viewBox="0 0 6 10"><rect x=".5" y=".5" width="5" height="9" rx="1" fill="none" stroke="#e4e6e8"/></svg>
    <span>+49 (0)5512 604</span>
  </div>
  <div class="item" style="left:453px">
    <svg width="10" height="7" viewBox="0 0 10 7"><rect width="10" height="7" fill="#e4e6e8"/><path d="M0 0l5 4 5-4" stroke="#22282e" fill="none"/></svg>
    <span>info@bramwelloq.com</span>
  </div>
  <div class="social"><span>Connect with Us</span><i class="dot"></i><i class="dot"></i><i class="dot"></i><i class="dot"></i></div>
</div>

<div class="abs header"></div>
<div class="abs photo-band" role="img" aria-label="Soft white office interior backdrop"></div>

<div class="abs logo"><span class="mark"></span><span>BRAMWELLOQ</span></div>
<a class="abs auth signin">Sign in</a>
<a class="abs auth register">Register</a>
<nav class="abs menu">
  <span>Home</span><span>About our school</span><span>Risk warning</span><span>FAQ</span><span>Trading Glossary</span><span>Contact</span>
</nav>

<div class="abs hero-frame"></div>
<div class="abs hero-image" role="img" aria-label="Businessman presenting a glowing world map with rising market charts"></div>
<form class="abs join">
  <h2>JOIN SCHOOL NOW!</h2>
  <div class="field" style="top:58px">First name</div>
  <div class="field" style="top:96px">Last name</div>
  <div class="field" style="top:134px">Email</div>
  <div class="agree"><span class="box"></span><span>Agree with our terms and conditions</span></div>
  <div class="submit">Submit</div>
</form>

<section class="abs features">
  <div class="feature" style="left:300px">
    <div class="icon"><svg width="14" height="14" viewBox="0 0 14 14"><circle cx="7" cy="6" r="3.5" fill="none" stroke="#fff" stroke-width="1.3"/><rect x="5.5" y="10" width="3" height="2.5" fill="#fff"/></svg></div>
    <h3>BEST TRADING<br>TIPS EVER</h3>
    <p>Consectetur adipisicing elit,<br>sed do eiusmod teor incididunt.</p>
  </div>
  <div class="feature" style="left:447px">
    <div class="icon"><svg width="14" height="14" viewBox="0 0 14 14"><rect x="5" y="1" width="8" height="5" rx="2" fill="#fff"/><circle cx="4" cy="8" r="2" fill="#fff"/><path d="M1 13a3 3 0 0 1 6 0z" fill="#fff"/></svg></div>
    <h3>SECRET TIPS<br>FROM EXPERT</h3>
    <p>Lorem ipsum dolor sit amet,<br>consectetur adipisicing elit.</p>
  </div>
  <div class="feature" style="left:598px">
    <div class="icon"><svg width="14" height="14" viewBox="0 0 14 14"><rect x="1" y="2" width="12" height="8" fill="none" stroke="#fff" stroke-width="1.2"/><path d="M3 8l3-3 2 2 3-3" stroke="#fff" fill="none"/><rect x="5" y="11" width="4" height="1.5" fill="#fff"/></svg></div>
    <h3>WE TEACH YOU HOW<br>TO TRADE ONLINE</h3>
    <p>Do eiusmod tempor incididunt<br>ut labore et dolore mna aliqua.</p>
  </div>
  <div class="feature" style="left:749px">
    <div class="icon"><svg width="14" height="14" viewBox="0 0 14 14"><circle cx="7" cy="7" r="5.5" fill="none" stroke="#fff" stroke-width="1.3"/><rect x="4.5" y="7" width="1.3" height="3" fill="#fff"/><rect x="6.4" y="5" width="1.3" height="5" fill="#fff"/><rect x="8.3" y="6" width="1.3" height="4" fill="#fff"/></svg></div>
    <h3>LEARN HOW TO<br>TRADE COMMODITIES</h3>
    <p>Sed do eiusmod tempor<br>incididunt ut labore et dolore.</p>
  </div>
  <div class="feature" style="left:898px">
    <div class="icon"><svg width="14" height="14" viewBox="0 0 14 14"><circle cx="7" cy="7" r="5.5" fill="none" stroke="#fff" stroke-width="1.3"/><circle cx="7" cy="6" r="1.6" fill="#fff"/><path d="M4 10.5a3 3 0 0 1 6 0z" fill="#fff"/></svg></div>
    <h3>LEARN HOW TO<br>BECOME A TRADER</h3>
    <p>Consecteur adipisiing elit, sed<br>do eiusmod tempor incididunt.</p>
  </div>
</section>

<section class="abs offer" role="img" aria-label="Trading floor scene in blue tint behind the offer text">
  <h2>WHAT DO WE OFFER</h2>
  <p>Nemo enim ipsam voluptatem quia voluptas sit aspernatur aut odit aut fugit, sed quia consequuntur magni dolores eos qui ratione voluptatem sequi nesciunt. Neque porro quisquam est, qui dolorem ipsum quia dolor sit amet, consectetur, adipisci velit, sed quia non numquam eius modi tempora incidunt ut labore et dolore magnam aliquam quaerat voluptatem. Ut enim ad minima veniam, quis nostrum exercitationem ullam corporis suscipit laboriosam, nisi ut aliquid exea commodi consequatur?</p>
</section>

<footer class="abs footer">
  <div class="col" style="left:251px">
    <h4>SITE NAVIGATION</h4>
    <ul>
      <li><i class="bullet"></i>Home</li>
      <li><i class="bullet"></i>About Us</li>
      <li><i class="bullet"></i>Risk Warning</li>
      <li><i class="bullet"></i>FAQ</li>
      <li><i class="bullet"></i>Trading Glossary</li>
      <li><i class="bullet"></i>Contact</li>
    </ul>
  </div>
  <div class="col connect" style="left:506px">
    <h4>CONNECT</h4>
    <ul>
      <li><i class="ring"></i>chirpline</li>
      <li><i class="ring"></i>friendwall</li>
      <li><i class="ring"></i>orbitcircle</li>
      <li><i class="ring"></i>workweb</li>
    </ul>
  </div>
  <div class="col" style="left:748px">
    <h4>WHY JOIN US</h4>
    <ul>
      <li><i class="bullet"></i>Best trading tips ever</li>
      <li><i class="bullet"></i>Secret tips from expert</li>
      <li><i class="bullet"></i>We teach you how to trade online</li>
      <li><i class="bullet"></i>Learn how to trade commodities</li>
      <li><i class="bullet"></i>Learn how to become trader</li>
    </ul>
  </div>
</footer>

<div class="abs bottombar">
  <span class="abs copyright">© Bramwelloq LCC. All Rights Reserved 2016</span>
  <span class="abs subscribe">SUBSCRIBE</span>
  <span class="abs sub-input">Your Email</span>
  <span class="abs sub-go">GO</span>
  <span class="abs legal">Terms of Use | Privacy Policy</span>
</div>

</body>
</html>
```